Falcrest security business card

Looking for a business card for my security company

Target Market(s)

Security

Industry/Entity Type

Security

Contact Information for Business Card

Name - Gil Marston. Title - General manager - direct 314 862.4490 website www. falcrestsecurityservices.example email - gil@ falcrestsecurityservices.example

Requirements
Must have
• Logo attached

```html
<!DOCTYPE html>
<html lang="en">
<head>
<meta charset="utf-8">
<title>Falcrest Security Services – Business Card</title>
<link rel="stylesheet" href="https://fonts.googleapis.com/css2?family=Lato:wght@400;700&display=swap">
<style>
  :root {
    --backdrop: #c8c8c8;
    --card: #000000;
    --gold: #d2ae62;
    --gold-light: #e8d29a;
    --gold-deep: #b88c3c;
  }
  * { margin: 0; padding: 0; box-sizing: border-box; }
  html, body {
    width: 1200px;
    height: 1200px;
    overflow: hidden;
    background: var(--backdrop);
    font-family: "Lato", sans-serif;
  }
  .card {
    position: absolute;
    width: 826px;
    height: 474px;
    background: var(--card);
  }
  .card--front { left: 188px; top: 91px; }
  .card--back { left: 186px; top: 635px; width: 828px; }

  .identity {
    position: absolute;
    right: 464px;
    top: 190px;
    text-align: right;
  }
  .identity__name {
    font-weight: 700;
    font-size: 44px;
    line-height: 1;
    letter-spacing: -0.5px;
    color: var(--gold-light);
  }
  .identity__title {
    margin-top: 10px;
    font-weight: 400;
    font-size: 20px;
    line-height: 1;
    color: var(--gold);
  }
  .divider {
    position: absolute;
    left: 389px;
    top: 203px;
    width: 2px;
    height: 69px;
    background: var(--gold);
  }
  .contacts {
    position: absolute;
    left: 417px;
    top: 198px;
    list-style: none;
  }
  .contacts__item {
    display: flex;
    align-items: center;
    height: 28.5px;
    font-size: 20px;
    color: var(--gold-light);
  }
  .contacts__icon {
    width: 18px;
    height: 18px;
    margin-right: 10px;
    flex: none;
  }
  .brand-name {
    position: absolute;
    font-weight: 700;
    color: var(--gold);
    white-space: nowrap;
    transform: translateX(-50%);
  }
  .brand-name--small {
    left: 697px;
    top: 390px;
    font-size: 26px;
    letter-spacing: 1px;
  }
  .brand-name--large {
    left: 414px;
    top: 190px;
    font-size: 72px;
    letter-spacing: 2px;
  }
  .website {
    position: absolute;
    left: 0;
    right: 0;
    top: 410px;
    display: flex;
    align-items: center;
    justify-content: center;
    gap: 12px;
  }
  .website__rule {
    width: 174px;
    height: 2px;
    background: var(--gold);
  }
  .website__url {
    font-size: 21px;
    color: var(--gold-light);
  }
</style>
</head>
<body>

<section class="card card--front">
  <div class="identity">
    <p class="identity__name">GIL MARSTON</p>
    <p class="identity__title">General Manager</p>
  </div>
  <div class="divider"></div>
  <ul class="contacts">
    <li class="contacts__item">
      <svg class="contacts__icon" viewBox="0 0 24 24" fill="none" stroke="var(--gold)" stroke-width="2.2" stroke-linecap="round" stroke-linejoin="round" aria-hidden="true">
        <path d="M5 3h4l2 5-2.5 1.5a11 11 0 0 0 6 6L16 13l5 2v4a2 2 0 0 1-2 2A16 16 0 0 1 3 5a2 2 0 0 1 2-2z"/>
        <path d="M15 3a6 6 0 0 1 6 6M15 7a2 2 0 0 1 2 2"/>
      </svg>
      <span>314 862.4490</span>
    </li>
    <li class="contacts__item">
      <svg class="contacts__icon" viewBox="0 0 24 24" aria-hidden="true">
        <rect x="2" y="5" width="20" height="14" fill="var(--gold)"/>
        <path d="M2 5l10 8 10-8M2 19l7-7M22 19l-7-7" fill="none" stroke="#000" stroke-width="1.8"/>
      </svg>
      <span>gil@ falcrestsecurityservices.example</span>
    </li>
    <li class="contacts__item">
      <svg class="contacts__icon" viewBox="0 0 24 24" fill="none" stroke="var(--gold)" stroke-width="1.8" aria-hidden="true">
        <circle cx="12" cy="12" r="10"/>
        <ellipse cx="12" cy="12" rx="4.5" ry="10"/>
        <path d="M2 12h20M4 7h16M4 17h16"/>
      </svg>
      <span>www. falcrestsecurityservices.example</span>
    </li>
  </ul>
  <p class="brand-name brand-name--small">FALCREST</p>
</section>

<section class="card card--back">
  <p class="brand-name brand-name--large">FALCREST</p>
  <div class="website">
    <span class="website__rule"></span>
    <span class="website__url">www. falcrestsecurityservices.example</span>
    <span class="website__rule"></span>
  </div>
</section>

</body>
</html>
```